Wine Tasting Event

We need a flyer design for a wine tasting event on Friday, February 14th. This is NOT a Valentine's themed event. It's merely an event for both singles and couples who do not want to drop a ton of money on a traditional meal at a fine restaurant. There will be good wines to taste, light snacks, info sessions on how to taste/appreciate good wine, live music, and a full bar in addition to the wine.

The event is called "Poured on the Millrace" and will be held at a venue overlooking the beautiful Harwick Greenway path.

We had an initial idea of a Large Wine cork taking up the majority of the flyer, with all of the information printed on it (as if it were a part of the cork). We are not designers, but have attached the initial attempt at the idea. Warning - It's bad.

Target Market(s)

Men and Women aged 21-35.

Industry/Entity Type

Restaurant

Requirements
Must have
• Name: Poured on the Millrace
Date: Friday, February 14th
Logo: Dunmore Play and Mixer League (See Attached File)

*NOTE Logo should not be a focal point of design. Just needs to be somewhere on the flyer. Can be substituted fo "Dunmore Play and Mixer League Presents"

Needs to be adaptable for 4"x6", 8.5"x11", and 11"x17"
Nice to have
• Wine cork, bottle, or glass. Something Atlanta related, or related to the Harwick Greenway.
Should not have
• Anything related to Valentine's Day

```html
<!DOCTYPE html>
<html lang="en">
<head>
<meta charset="utf-8">
<title>Poured on the Millrace – Wine Tasting Event</title>
<link rel="stylesheet" href="https://fonts.googleapis.com/css2?family=Arimo:ital,wght@0,700;1,700&family=Lobster&family=Alfa+Slab+One&display=swap">
<style>
  :root {
    --ink: #0b0b0b;
    --deep: #161616;
    --cork-light: #d9b98a;
    --cork-mid: #a98556;
    --cork-dark: #5c4428;
    --steel: #8b8a86;
    --silver-top: #ffffff;
    --silver-mid: #cfd3d6;
    --silver-low: #8f969b;
    --wine-red: #e0141b;
    --white: #ffffff;
    --gold: #f6c21a;
    --glass-green: #2c5a3e;
  }
  * { margin: 0; padding: 0; box-sizing: border-box; }
  html, body { width: 927px; height: 1200px; overflow: hidden; background: var(--ink); }
  .flyer {
    position: relative;
    width: 927px;
    height: 1200px;
    overflow: hidden;
    background: var(--ink);
    font-family: "Arimo", Arial, sans-serif;
  }
  .flyer__photo {
    position: absolute;
    inset: 0;
    background:
      radial-gradient(ellipse 230px 420px at 640px 690px, var(--cork-light) 0%, var(--cork-mid) 55%, rgba(92,68,40,0) 100%),
      radial-gradient(ellipse 260px 700px at 90px 800px, rgba(139,138,134,0.55) 0%, rgba(139,138,134,0) 100%),
      radial-gradient(ellipse 300px 200px at 80px 1150px, rgba(44,90,62,0.7) 0%, rgba(44,90,62,0) 100%),
      linear-gradient(180deg, var(--deep) 0%, var(--ink) 100%);
  }
  .title {
    position: absolute;
    top: 52px;
    left: 0;
    width: 880px;
    text-align: right;
    font-weight: 700;
    font-size: 168px;
    letter-spacing: -6px;
    line-height: 1;
    background: linear-gradient(180deg, var(--silver-top) 0%, var(--silver-mid) 45%, var(--silver-low) 100%);
    -webkit-background-clip: text;
    background-clip: text;
    color: transparent;
    -webkit-text-stroke: 3px var(--ink);
  }
  .subtitle {
    position: absolute;
    top: 212px;
    right: 62px;
    font-family: "Lobster", cursive;
    font-size: 82px;
    line-height: 1;
    color: var(--wine-red);
    -webkit-text-stroke: 2px var(--white);
    paint-order: stroke fill;
    text-shadow: 3px 3px 0 var(--ink);
  }
  .headline {
    position: absolute;
    top: 578px;
    left: 160px;
    width: 720px;
    text-align: center;
    font-style: italic;
    font-weight: 700;
    font-size: 60px;
    line-height: 66px;
    color: var(--wine-red);
    -webkit-text-stroke: 6px var(--white);
    paint-order: stroke fill;
    text-shadow: 4px 4px 4px rgba(0,0,0,0.8);
    letter-spacing: -1px;
  }
  .presenter {
    position: absolute;
    top: 830px;
    left: 596px;
    width: 280px;
    text-align: center;
    font-weight: 700;
    font-size: 24px;
    line-height: 28px;
    color: var(--wine-red);
    text-transform: uppercase;
  }
  .details {
    position: absolute;
    top: 970px;
    left: 36px;
    width: 580px;
    font-style: italic;
    font-weight: 700;
    font-size: 27px;
    line-height: 36.5px;
    letter-spacing: -0.6px;
    color: var(--white);
    -webkit-text-stroke: 5px var(--ink);
    paint-order: stroke fill;
  }
  .join-badge {
    position: absolute;
    left: 651px;
    top: 930px;
    width: 210px;
    height: 210px;
  }
</style>
</head>
<body>
<main class="flyer">
  <div class="flyer__photo" role="img" aria-label="Close-up photograph of a corkscrew twisting into a wine cork against a dark background"></div>

  <h1 class="title">POURED</h1>
  <p class="subtitle">on the Millrace</p>

  <h2 class="headline">Wine Tasting Event<br>on Friday, February 14th</h2>

  <p class="presenter">Dunmore Play<br>and Mixer League</p>

  <p class="details">There will be good wines to taste, light snacks, info sessions on how to taste/appreciate good wine, live music, and a full bar in addition to the wine.</p>

  <svg class="join-badge" viewBox="0 0 210 210" aria-label="Join now">
    <circle cx="105" cy="105" r="102" fill="var(--ink)"/>
    <circle cx="105" cy="105" r="96" fill="var(--gold)"/>
    <circle cx="105" cy="105" r="82" fill="var(--ink)"/>
    <circle cx="105" cy="105" r="74" fill="var(--white)"/>
    <g transform="rotate(32 105 105)" font-family="'Alfa Slab One', serif" font-size="42" text-anchor="middle" fill="var(--gold)" stroke="var(--ink)" stroke-width="3" paint-order="stroke fill">
      <text x="105" y="98">JOIN</text>
      <text x="105" y="142">NOW</text>
    </g>
  </svg>
</main>
</body>
</html>
```